Yard sign

I want it to look similar to this one,

change name to DRAVEK and submit new ideas

Also would like to improvise a bit. let's not make exactly the same thing

would like to change to: Connecticut #1 Company

also change phone to 203-555-0147
and website to
dravekllc.com

this is yard sign. size is 24' Width and 32' Height

Target Market(s)

Roof

Industry/Entity Type

Roofing

Requirements
Must have
• similar colors or add something new

```html
<!DOCTYPE html>
<html lang="en">
<head>
<meta charset="utf-8">
<title>Dravek – Yard Sign</title>
<link rel="stylesheet" href="https://fonts.googleapis.com/css2?family=Archivo:wght@700;800&family=Archivo+Black&display=swap">
<style>
  :root {
    --sign-yellow: #fecb0b;
    --sign-black: #000000;
    --sign-red: #ec1c24;
    --sign-white: #ffffff;
  }
  html, body {
    margin: 0;
    padding: 0;
    width: 900px;
    height: 1200px;
    overflow: hidden;
    background: var(--sign-black);
  }
  .yard-sign { display: block; width: 900px; height: 1200px; }
  .band-top { fill: var(--sign-yellow); }
  .band-bottom { fill: var(--sign-black); }
  .tagline {
    font-family: "Archivo", Arial, sans-serif;
    font-weight: 800;
    fill: var(--sign-black);
  }
  .headline { font-family: "Archivo Black", Arial, sans-serif; }
  .headline-fill { fill: var(--sign-black); }
  .headline-echo { fill: none; stroke: var(--sign-red); stroke-width: 3.5; }
  .chevron { fill: var(--sign-red); }
  .chevron-shadow { fill: var(--sign-black); }
  .frame-line { fill: none; stroke: var(--sign-yellow); stroke-width: 4; }
  .brand-name { font-family: "Archivo Black", Arial, sans-serif; }
  .brand-fill { fill: var(--sign-red); }
  .brand-echo { fill: none; stroke: var(--sign-yellow); stroke-width: 4; }
  .phone-box { fill: var(--sign-yellow); }
  .phone-number {
    font-family: "Archivo Black", Arial, sans-serif;
    fill: var(--sign-black);
  }
  .web-address {
    font-family: "Archivo", Arial, sans-serif;
    font-weight: 700;
    fill: var(--sign-white);
  }
</style>
</head>
<body>
<svg class="yard-sign" viewBox="0 0 900 1200" xmlns="http://www.w3.org/2000/svg">
  <rect class="band-top" x="0" y="0" width="900" height="480"/>
  <rect class="band-bottom" x="0" y="480" width="900" height="720"/>

  <text class="tagline" x="450" y="120" font-size="96" text-anchor="middle" textLength="700" lengthAdjust="spacingAndGlyphs">Connecticut #1</text>

  <g class="headline">
    <text class="headline-echo" x="456" y="300" font-size="168" text-anchor="middle" textLength="780" lengthAdjust="spacingAndGlyphs">COMPANY</text>
    <text class="headline-fill" x="450" y="306" font-size="168" text-anchor="middle" textLength="780" lengthAdjust="spacingAndGlyphs">COMPANY</text>
  </g>

  <g class="chevrons">
    <g transform="translate(-11,6)">
      <polygon class="chevron-shadow" points="50,370 156,370 216,480 156,590 50,590 110,480"/>
      <polygon class="chevron-shadow" points="208,370 314,370 374,480 314,590 208,590 268,480"/>
      <polygon class="chevron-shadow" points="366,370 472,370 532,480 472,590 366,590 426,480"/>
      <polygon class="chevron-shadow" points="524,370 630,370 690,480 630,590 524,590 584,480"/>
      <polygon class="chevron-shadow" points="682,370 788,370 848,480 788,590 682,590 742,480"/>
    </g>
    <polygon class="chevron" points="50,370 156,370 216,480 156,590 50,590 110,480"/>
    <polygon class="chevron" points="208,370 314,370 374,480 314,590 208,590 268,480"/>
    <polygon class="chevron" points="366,370 472,370 532,480 472,590 366,590 426,480"/>
    <polygon class="chevron" points="524,370 630,370 690,480 630,590 524,590 584,480"/>
    <polygon class="chevron" points="682,370 788,370 848,480 788,590 682,590 742,480"/>
  </g>

  <rect class="frame-line" x="30" y="630" width="840" height="540"/>

  <g class="brand-name">
    <text class="brand-echo" x="456" y="830" font-size="210" text-anchor="middle" textLength="740" lengthAdjust="spacingAndGlyphs">DRAVEK</text>
    <text class="brand-fill" x="450" y="836" font-size="210" text-anchor="middle" textLength="740" lengthAdjust="spacingAndGlyphs">DRAVEK</text>
  </g>

  <rect class="phone-box" x="70" y="888" width="760" height="140"/>
  <text class="phone-number" x="450" y="1000" font-size="112" text-anchor="middle" textLength="700" lengthAdjust="spacingAndGlyphs">203-555-0147</text>

  <text class="web-address" x="450" y="1128" font-size="84" text-anchor="middle" textLength="520" lengthAdjust="spacingAndGlyphs">dravekllc.com</text>
</svg>
</body>
</html>
```